Label Design for Nuts package*

Develop the design for a label for nuts sold in a paperbag.

you can find our website here: www.brotkorn-snack.de.
Here comes the link to our catalogue: https://www.blattwerk-docs.com/de/document/read/48172095/brotkorn-premium-snacks-gesamtkatalog-2019

With this product we are targeting private customers who want to buy nuts with plastic free packaging online.
The colours of the label should fit the brown paper bag.

```html
<!DOCTYPE html>
<html lang="de">
<head>
<meta charset="utf-8">
<title>brotkorn – Sonnenfund Etikett</title>
<link rel="stylesheet" href="https://fonts.googleapis.com/css2?family=Catamaran:wght@300;400;600&family=Cormorant+Garamond:wght@500;600&display=swap">
<style>
  :root {
    --page: #efe9e0;
    --label-beige: #d6c3a6;
    --label-beige-edge: #cbb697;
    --panel-navy: #1c2230;
    --copper: #a8674f;
    --copper-light: #d6aa8a;
    --cream: #eadbc9;
    --rule: #8a7565;
    --rim: #8d8780;
    --nut-light: #e6cfa8;
    --nut-mid: #b9773f;
    --nut-dark: #6e3b1d;
  }
  * { box-sizing: border-box; margin: 0; padding: 0; }
  html, body { width: 1049px; height: 1200px; overflow: hidden; background: var(--page); }
  .label {
    position: absolute; left: 27px; top: 48px;
    width: 994px; height: 1104px;
    background: var(--label-beige);
    overflow: hidden;
    box-shadow: inset 0 0 0 1px var(--label-beige-edge);
  }
  .panel {
    position: absolute; left: 195px; top: 0;
    width: 605px; height: 100%;
    background: var(--panel-navy);
    box-shadow: 0 0 0 6px var(--label-beige), 0 0 0 8px var(--copper-light);
    text-align: center;
  }
  .brand-dot {
    position: absolute; top: 62px; left: 50%; margin-left: -34px;
    width: 68px; height: 68px; border-radius: 50%;
    background: var(--copper);
  }
  .brand {
    position: absolute; top: 150px; left: 0; width: 100%;
    font-family: "Catamaran", sans-serif; font-weight: 300;
    font-size: 70px; letter-spacing: 3px; line-height: 1;
    color: var(--copper);
  }
  .tagline {
    position: absolute; top: 240px; left: 0; width: 100%;
    font-family: "Cormorant Garamond", serif; font-weight: 600;
    font-size: 21px; letter-spacing: 2px; color: var(--cream);
  }
  .tagline-rule {
    position: absolute; top: 272px; left: 50%; margin-left: -112px;
    width: 224px; height: 1px; background: var(--rule);
  }
  .product-name {
    position: absolute; top: 358px; left: 0; width: 100%;
    font-family: "Catamaran", sans-serif; font-weight: 600;
    font-size: 80px; line-height: 1; letter-spacing: 1px;
    color: var(--copper-light);
  }
  .rule { position: absolute; left: 66px; width: 473px; height: 2px; background: var(--rule); }
  .rule.top { top: 495px; }
  .rule.bottom { top: 612px; }
  .description {
    position: absolute; top: 508px; left: 0; width: 100%;
    font-family: "Catamaran", sans-serif; font-weight: 400;
    font-size: 37px; line-height: 43px; color: var(--cream);
  }
  .window { position: absolute; left: 0; top: 0; }
  .weight {
    position: absolute; left: 428px; top: 987px;
    width: 138px; height: 138px; border-radius: 50%;
    background: var(--panel-navy);
    font-family: "Catamaran", sans-serif; font-weight: 400;
    font-size: 24px; color: #fff; text-align: center;
    padding-top: 42px;
  }
</style>
</head>
<body>
  <div class="label">
    <div class="panel">
      <div class="brand-dot"></div>
      <div class="brand">brotkorn</div>
      <div class="tagline">PREMIUM SNACKS</div>
      <div class="tagline-rule"></div>
      <h1 class="product-name">SONNENFUND</h1>
      <div class="rule top"></div>
      <p class="description">ofengeröstete<br>cashewkerne mit curry</p>
      <div class="rule bottom"></div>
    </div>

    <svg class="window" width="994" height="1104" viewBox="0 0 994 1104">
      <defs>
        <radialGradient id="nutTones" cx="50%" cy="40%" r="60%">
          <stop offset="0%" stop-color="#e6cfa8"/>
          <stop offset="55%" stop-color="#b9773f"/>
          <stop offset="100%" stop-color="#6e3b1d"/>
        </radialGradient>
      </defs>
      <circle cx="497" cy="1104" r="413" fill="#8d8780"/>
      <circle cx="497" cy="1104" r="405" fill="url(#nutTones)" role="img" aria-label="Foto einer Nussmischung mit Cashewkernen, Mandeln, Haselnüssen und Walnüssen"/>
    </svg>

    <div class="weight">250gm</div>
  </div>
</body>
</html>
```